Business card for dental office with laser therapy / dental facial esthetic

A simple logo which should signifies
Dentistry intraoral as primary and with extended extraoral cosmetic facial esthetic services ( regenerative skincare ) which enhance Beauty as whole .
Conservative high tech approach by using laser intraoral and extraoral limited to face and neck
Front Face :May be black background with neon blue / purplish Rim signifies laser ( ?) & abstract face profile and tooth or Apple design in one ? / see upload inspiration design
Back side : simple appointment slots with date and time / white background / black letter

Color : black/ neon blue/ purplish and gold incorporate for logo design
Final design : dental / esthetic / modern high tech and safe

Target Market(s)

Dental Patients who seeks more high end cosmetic treatment

Industry/Entity Type

Health Care

Contact Information for Business Card

Esthetic modern elegant looking
Logo and office must haves important informations

Logo Text

Family & Cosmetic Dentistry

Font styles to use
Script

Requirements
Must have
• Name of practice and all important informations
• Family & Cosmetic Dentistry
• Lan B. Okafor DMD,PC
• 38412 Brantley Court ,ste.207
• Cedar Hollow ,VA 20391
• Ph. 703-555-0187
• Fax 703-5550193
Nice to have
• More abstract
• Front : black back ground with neon blue rim (signifies laser therapy)
• Logo can also be golden gold / neon blue
• Address & Infos can be white
Should not have
• Not to busy looking

```html
<!DOCTYPE html>
<html lang="en">
<head>
<meta charset="utf-8">
<title>Lumivea Laser Therapy – Business Card</title>
<link rel="stylesheet" href="https://fonts.googleapis.com/css2?family=Questrial&display=swap">
<style>
  :root {
    --stage: #1c1c1e;
    --card-black: #050505;
    --card-white: #ffffff;
    --gold: #d8b65a;
    --gold-soft: #c9a74e;
    --ink: #111111;
    --ink-grey: #8a8a8e;
    --violet: #6a3fb0;
    --magenta: #c04fa6;
    --rose: #e3879a;
    --lemon: #f1e25a;
    --face-tone: #161318;
  }
  * { box-sizing: border-box; margin: 0; padding: 0; }
  html, body {
    width: 1200px; height: 800px; overflow: hidden;
    background: var(--stage);
    font-family: "Questrial", "Century Gothic", sans-serif;
  }
  .canvas { position: relative; width: 1200px; height: 800px; }

  .card {
    position: absolute; width: 540px; height: 309px; overflow: hidden;
  }

  /* Back: appointment card */
  .card--back { left: 40px; top: 110px; background: var(--card-white); color: var(--ink); }
  .slot {
    position: absolute; left: 48px; display: flex; align-items: baseline;
    font-size: 14px;
  }
  .slot--date { top: 172px; }
  .slot--time { top: 208px; }
  .slot__label { margin-right: 6px; }
  .slot__line {
    width: 330px; border-bottom: 1.5px dotted var(--ink); transform: translateY(-3px);
  }
  .slot--time .slot__line { width: 310px; }
  .brand--back {
    position: absolute; right: 40px; bottom: 52px; text-align: right; color: var(--ink-grey);
  }
  .brand--back .brand__name { font-size: 26px; letter-spacing: 3px; }
  .brand--back .brand__sub { font-size: 10px; letter-spacing: 1.5px; }

  /* Front: practice card */
  .card--front { left: 620px; top: 380px; background: var(--card-black); color: var(--gold); }
  .face-art {
    position: absolute; right: 20px; top: 0; width: 200px; height: 210px;
    background: radial-gradient(ellipse at 55% 45%, var(--face-tone) 0%, #0b0a0c 60%, transparent 80%);
  }
  .brand--front { position: absolute; left: 44px; top: 70px; color: var(--gold); }
  .brand--front .brand__mark {
    display: inline-block; width: 12px; height: 12px; border-radius: 50%;
    background: var(--gold); margin-right: 12px; vertical-align: middle;
  }
  .brand--front .brand__name { font-size: 42px; letter-spacing: 5px; vertical-align: middle; }
  .brand--front .brand__sub {
    display: block; font-size: 15px; letter-spacing: 3px; margin: 4px 0 0 150px;
  }
  .doctor { position: absolute; left: 40px; top: 182px; }
  .doctor__name { font-size: 18px; }
  .doctor__specialty { font-size: 12.5px; margin-top: 2px; }
  .address {
    position: absolute; right: 38px; top: 186px; text-align: right; font-size: 12.5px; line-height: 1.4;
  }
  .rule {
    position: absolute; left: 40px; right: 38px; top: 228px; height: 1px;
    background: linear-gradient(90deg, var(--gold-soft) 0%, var(--gold-soft) 40%, var(--violet) 100%);
  }
  .contact { position: absolute; left: 40px; top: 240px; font-size: 13px; line-height: 1.4; }
  .laser-band {
    position: absolute; left: 0; right: 0; bottom: 0; height: 10px;
    background: linear-gradient(90deg, var(--lemon) 0%, var(--rose) 25%, var(--magenta) 50%, var(--violet) 100%);
  }
</style>
</head>
<body>
<main class="canvas">

  <section class="card card--back" aria-label="Appointment side">
    <div class="slot slot--date"><span class="slot__label">Date:</span><span class="slot__line"></span></div>
    <div class="slot slot--time"><span class="slot__label">Time:</span><span class="slot__line"></span></div>
    <div class="brand brand--back">
      <div class="brand__name">Lumivea</div>
      <div class="brand__sub">Laser Therapy</div>
    </div>
  </section>

  <section class="card card--front" aria-label="Practice side">
    <div class="face-art" role="img" aria-label="Faint abstract profile silhouette artwork"></div>
    <div class="brand brand--front">
      <span class="brand__mark"></span><span class="brand__name">Lumivea</span>
      <span class="brand__sub">Laser Therapy</span>
    </div>
    <div class="doctor">
      <div class="doctor__name">Lan B. Okafor DMD,PC</div>
      <div class="doctor__specialty">Family &amp; Cosmetic Dentistry</div>
    </div>
    <div class="address">
      <div>38412 Brantley Court ,ste.207</div>
      <div>Cedar Hollow ,VA 20391</div>
    </div>
    <div class="rule"></div>
    <div class="contact">
      <div>Ph. 703-555-0187</div>
      <div>Fax 703-5550193</div>
    </div>
    <div class="laser-band"></div>
  </section>

</main>
</body>
</html>
```